Pelbrook Metal Roofing INC.

Hello,
I am working with a local business to design them a new website. The designer I had worked with moved to colorado and has taken a new job. He recommended that I try posting my new jobs on here. I would need a design and assistance setting the site up on my host nimbus server. I work by myself and handle the sales side of things and need a designer that can help me out.
This company is a metal roofing business. The current page I made for them is www.pelbrookmetalinc.example

They would like the new site to be similar to http://www.tamblecreekalloy.example

Please let me know if this is something that you could do for us.
Updates

the company wants the site to look very similar to this http://www.tamblecreekalloy.exampleis that something you could do, please get in touch with me.Thanks Added Tuesday, January 10, 2017

Industry/Entity Type

Business

Font styles to use
Sans Serif

Colors
ed252d

Requirements
Must have
• the company wants the site to look very similar to this
• http://www.tamblecreekalloy.example
• is that something you could do, please get in touch with me.
• Thanks

```html
<!DOCTYPE html>
<html lang="en">
<head>
<meta charset="utf-8">
<title>Pelbrook Metal Inc</title>
<link href="https://fonts.googleapis.com/css2?family=Lato:wght@300;400;700;900&display=swap" rel="stylesheet">
<style>
:root{
  --red:#ed252d;
  --red-dark:#c41820;
  --charcoal:#2b2b2b;
  --footer:#262626;
  --footer-line:#3a3a3a;
  --page:#ececec;
  --panel:#f4f4f4;
  --text:#444;
  --muted:#888;
  --white:#fff;
}
*{box-sizing:border-box;margin:0;padding:0}
html,body{width:724px;height:1200px;overflow:hidden}
body{font-family:"Lato",Arial,sans-serif;color:var(--text);background:var(--page);position:relative}
.topbar{position:absolute;left:0;top:0;width:724px;height:60px;background:var(--charcoal);overflow:hidden}
.topbar-red{position:absolute;right:0;top:0;width:460px;height:60px;background:var(--red);clip-path:polygon(40px 0,100% 0,100% 100%,0 100%)}
.brand{position:absolute;left:40px;top:12px;border:1px solid #777;padding:6px 12px;color:var(--white);font-weight:700;font-size:15px;letter-spacing:.5px}
.phones{position:absolute;right:140px;top:20px;display:flex;gap:24px;color:var(--white);font-size:11px;font-weight:700}
.phone{display:flex;align-items:center;gap:6px}
.quote-btn{position:absolute;right:40px;top:16px;background:var(--white);color:var(--red);font-size:10px;font-weight:900;padding:6px 10px;letter-spacing:.5px}
.nav{position:absolute;left:60px;top:60px;width:628px;height:50px;background:var(--white);display:flex;align-items:center;padding:0 10px;box-shadow:0 2px 4px rgba(0,0,0,.12)}
.nav a{font-size:11px;font-weight:700;color:#555;text-decoration:none;padding:8px 12px;letter-spacing:.3px}
.nav a.active{background:var(--red);color:var(--white)}
.search{margin-left:auto;width:130px;height:26px;border:1px solid #ccc;display:flex;align-items:center;justify-content:space-between;padding:0 8px;font-size:9px;color:var(--muted)}
.hero{position:absolute;left:96px;top:118px;width:592px;height:262px;background:var(--white);display:flex;box-shadow:0 2px 6px rgba(0,0,0,.12)}
.hero-photo{width:346px;margin:8px;background:linear-gradient(180deg,#d9d4cb 0%,#c7ab84 55%,#8f7a5a 80%,#b9b4aa 100%)}
.hero-list{flex:1;padding:6px 10px 0 4px;display:flex;flex-direction:column;gap:10px}
.hero-item{padding:8px 10px}
.hero-item.featured{background:var(--red);color:var(--white);margin-left:-14px}
.hero-item h3{font-size:12px;font-weight:900;color:var(--red);line-height:1.2;text-transform:uppercase}
.hero-item.featured h3{color:var(--white)}
.hero-item p{font-size:7.5px;line-height:1.4;margin-top:4px;color:var(--muted)}
.hero-item.featured p{color:#ffe3e3}
.intro{position:absolute;left:0;top:400px;width:724px;text-align:center}
.intro h1{font-size:38px;font-weight:300;color:var(--red);letter-spacing:1.5px}
.intro h2{font-size:17px;font-weight:300;color:#666;letter-spacing:1px;margin-top:2px}
.products-band{position:absolute;left:0;top:475px;width:724px;height:290px;background:var(--panel)}
.section-title{display:flex;align-items:center;gap:10px;font-size:21px;font-weight:300;color:#555;text-transform:uppercase;letter-spacing:.5px}
.section-title::before{content:"";width:4px;height:20px;background:var(--red)}
.section-title::after{content:"";flex:1;height:1px;background:#d4d4d4}
.featured-title{position:absolute;left:48px;top:30px;width:628px}
.carousel-arrow{position:absolute;top:175px;width:16px;height:34px;background:#cfcfcf;display:flex;align-items:center;justify-content:center}
.product{position:absolute;top:78px;width:192px;height:172px;text-align:center}
.product-img{height:134px;position:relative;display:flex;align-items:center;justify-content:center}
.product-name{font-size:11px;font-weight:700;color:#555;margin-top:14px;letter-spacing:.3px}
.view-details{background:rgba(255,255,255,.9);font-size:9px;padding:5px 10px;color:#333}
.about{position:absolute;left:48px;top:775px;width:382px}
.about p{font-size:8px;line-height:1.7;color:var(--muted);margin-top:20px;padding-right:10px}
.btn-dark{display:inline-block;background:#555;color:var(--white);font-size:9px;font-weight:700;padding:6px 12px;margin-top:14px}
.downloads{position:absolute;left:462px;top:775px;width:214px}
.downloads ul{list-style:none;margin-top:14px}
.downloads li{display:flex;align-items:center;gap:8px;font-size:8.5px;color:#555;padding:5px 0}
.footer{position:absolute;left:0;top:993px;width:724px;height:207px;background:var(--footer);color:#bbb;display:flex;padding:22px 48px 0;gap:34px}
.footer-col{flex:1}
.footer-col h4{font-size:11px;font-weight:700;color:var(--white);letter-spacing:.5px;padding-bottom:8px;border-bottom:1px solid var(--footer-line);text-transform:uppercase}
.project{display:flex;gap:8px;margin-top:10px;align-items:center}
.project-thumb{width:34px;height:26px;background:linear-gradient(135deg,#6f7d5a,#a89572)}
.project p{font-size:7.5px;line-height:1.4}
.footer-col .blurb{font-size:7.5px;line-height:1.6;margin-top:12px}
.email-field{margin-top:12px;height:22px;background:#3a3a3a;font-size:7.5px;color:#888;display:flex;align-items:center;padding:0 8px}
.subscribe{display:inline-block;background:var(--red);color:var(--white);font-size:8px;font-weight:900;padding:5px 12px;margin-top:10px}
.company{font-size:12px;font-weight:700;color:var(--white);margin-top:14px;letter-spacing:.4px}
.contact-line{display:flex;align-items:center;gap:6px;font-size:8px;margin-top:7px}
.hours-title{font-size:8px;font-weight:700;color:var(--white);margin-top:12px}
.hours{font-size:7.5px;line-height:1.6;margin-top:4px}
.hours-row{display:flex;justify-content:space-between}
.hours-row strong{color:var(--white);font-weight:700}
</style>
</head>
<body>
<header class="topbar">
  <div class="topbar-red"></div>
  <div class="brand">PELBROOK METAL INC</div>
  <div class="phones">
    <span class="phone"><svg width="11" height="11" viewBox="0 0 24 24"><path fill="#fff" d="M6.6 10.8a15 15 0 006.6 6.6l2.2-2.2c.3-.3.7-.4 1-.2 1.1.4 2.3.6 3.6.6.6 0 1 .4 1 1V20c0 .6-.4 1-1 1C10.6 21 3 13.4 3 4c0-.6.4-1 1-1h3.5c.6 0 1 .4 1 1 0 1.3.2 2.5.6 3.6.1.3 0 .7-.2 1z"/></svg>555-201-3487</span>
    <span class="phone"><svg width="11" height="11" viewBox="0 0 24 24"><path fill="#fff" d="M6.6 10.8a15 15 0 006.6 6.6l2.2-2.2c.3-.3.7-.4 1-.2 1.1.4 2.3.6 3.6.6.6 0 1 .4 1 1V20c0 .6-.4 1-1 1C10.6 21 3 13.4 3 4c0-.6.4-1 1-1h3.5c.6 0 1 .4 1 1 0 1.3.2 2.5.6 3.6.1.3 0 .7-.2 1z"/></svg>555-201-3922</span>
  </div>
  <div class="quote-btn">GET A QUOTE</div>
</header>

<nav class="nav">
  <a class="active">HOME</a><a>ABOUT US</a><a>PRODUCTS</a><a>PROJECT GALLERY</a><a>CONTACT</a>
  <div class="search">Search keyword<svg width="10" height="10" viewBox="0 0 24 24"><circle cx="10" cy="10" r="6" fill="none" stroke="#888" stroke-width="2.5"/><path d="M15 15l6 6" stroke="#888" stroke-width="2.5"/></svg></div>
</nav>

<section class="hero">
  <div class="hero-photo" role="img" aria-label="Post frame building under construction with timber trusses and bare trees"></div>
  <div class="hero-list">
    <div class="hero-item featured"><h3>Complete post frame building packages</h3><p>Talk to us to quote a full frame kit built for your site.</p></div>
    <div class="hero-item"><h3>Residential metal roofing</h3><p>Durable steel roof panels in a wide variety of colours and trims.</p></div>
    <div class="hero-item"><h3>Commercial and agri-cultural applications</h3><p>Steel siding and roofing sized for shops, barns and storage buildings.</p></div>
  </div>
</section>

<section class="intro">
  <h1>MANUFACTURERS</h1>
  <h2>QUALITY BUILDING COMPONENTS</h2>
</section>

<section class="products-band">
  <div class="section-title featured-title">Featured Products</div>
  <div class="carousel-arrow" style="left:8px"><svg width="8" height="12"><path d="M7 1L2 6l5 5" stroke="#fff" stroke-width="2" fill="none"/></svg></div>
  <div class="carousel-arrow" style="right:8px"><svg width="8" height="12"><path d="M1 1l5 5-5 5" stroke="#fff" stroke-width="2" fill="none"/></svg></div>
  <div class="product" style="left:48px">
    <div class="product-img" role="img" aria-label="Red metal roof panels" style="background:linear-gradient(160deg,#e24c4f,#b5262b)"><span class="view-details">View Details</span></div>
    <div class="product-name">PRODUCT NAME</div>
  </div>
  <div class="product" style="left:266px">
    <div class="product-img" role="img" aria-label="Green metal roof on a building" style="background:linear-gradient(160deg,#c9d4db 0%,#5f8f7c 55%,#3f6b5b 100%)"></div>
    <div class="product-name">PRODUCT NAME</div>
  </div>
  <div class="product" style="left:484px">
    <div class="product-img" role="img" aria-label="Red barn with white trim" style="background:linear-gradient(180deg,#cfdbe6 0%,#cfdbe6 30%,#b82a2d 31%,#a12326 80%,#8c9a6a 100%)"></div>
    <div class="product-name">PRODUCT NAME</div>
  </div>
</section>

<section class="about">
  <div class="section-title">About Pelbrook</div>
  <p>Pelbrook Metal is a family owned supplier of steel roofing and siding serving builders and homeowners across the region. Our panels are rolled to length in our own shop, so every order fits the job with less waste and fewer seams. We stock a broad range of colours, trims and fasteners, and our team can help plan post frame buildings from the ground up. Whether you need a single garage roof or a full agricultural package, we deliver quality components on time and at a fair price.</p>
  <span class="btn-dark">Click Here To Know More</span>
</section>

<section class="downloads">
  <div class="section-title">Downloads</div>
  <ul>
    <li><svg width="10" height="12" viewBox="0 0 10 12"><path d="M1 1h5l3 3v7H1z" fill="none" stroke="#ed252d"/></svg>Pelbrook Products Catalog &amp; Trim Details</li>
    <li><svg width="10" height="12" viewBox="0 0 10 12"><path d="M1 1h5l3 3v7H1z" fill="none" stroke="#ed252d"/></svg>Previous Product Catalog</li>
    <li><svg width="10" height="12" viewBox="0 0 10 12"><path d="M1 1h5l3 3v7H1z" fill="none" stroke="#ed252d"/></svg>Farm Building Brochure</li>
    <li><svg width="10" height="12" viewBox="0 0 10 12"><path d="M1 1h5l3 3v7H1z" fill="none" stroke="#ed252d"/></svg>Color Chart</li>
    <li><svg width="10" height="12" viewBox="0 0 10 12"><path d="M1 1h5l3 3v7H1z" fill="none" stroke="#ed252d"/></svg>Panel Warranty</li>
  </ul>
  <span class="btn-dark">View All</span>
</section>

<footer class="footer">
  <div class="footer-col">
    <h4>Recent Projects</h4>
    <div class="project"><div class="project-thumb" role="img" aria-label="Finished steel building"></div><p>New machine shed roofed in our galvalume panels this spring.</p></div>
    <div class="project"><div class="project-thumb" role="img" aria-label="Metal roofed home"></div><p>Farmhouse reroof with charcoal ribbed steel and matching trim.</p></div>
    <div class="project"><div class="project-thumb" role="img" aria-label="Post frame barn"></div><p>Complete post frame barn package delivered and built on site.</p></div>
  </div>
  <div class="footer-col">
    <h4>Newsletter Signup</h4>
    <p class="blurb">Join our mailing list for seasonal pricing, new colours and project tips sent straight to your inbox each month.</p>
    <div class="email-field">YOUR EMAIL ADDRESS</div>
    <span class="subscribe">SUBSCRIBE</span>
  </div>
  <div class="footer-col">
    <h4>Contact Info</h4>
    <div class="company">PELBROOK METAL INC</div>
    <div class="contact-line"><svg width="9" height="9" viewBox="0 0 24 24"><path fill="#ed252d" d="M6.6 10.8a15 15 0 006.6 6.6l2.2-2.2c.3-.3.7-.4 1-.2 1.1.4 2.3.6 3.6.6.6 0 1 .4 1 1V20c0 .6-.4 1-1 1C10.6 21 3 13.4 3 4c0-.6.4-1 1-1h3.5c.6 0 1 .4 1 1 0 1.3.2 2.5.6 3.6.1.3 0 .7-.2 1z"/></svg>555-201-3487</div>
    <div class="contact-line"><svg width="9" height="9" viewBox="0 0 24 24"><path fill="#ed252d" d="M6.6 10.8a15 15 0 006.6 6.6l2.2-2.2c.3-.3.7-.4 1-.2 1.1.4 2.3.6 3.6.6.6 0 1 .4 1 1V20c0 .6-.4 1-1 1C10.6 21 3 13.4 3 4c0-.6.4-1 1-1h3.5c.6 0 1 .4 1 1 0 1.3.2 2.5.6 3.6.1.3 0 .7-.2 1z"/></svg>555-201-3922</div>
    <div class="hours-title">WORKING HOURS</div>
    <div class="hours">
      <div>Weekdays: 7:30am - 4:30pm</div>
      <div class="hours-row"><span>Saturday: 8am - 11am</span><strong>Sunday: Closed</strong></div>
    </div>
  </div>
</footer>
</body>
</html>
```